Business Card design for consulting company

We are a small consulting company (Valmor Consulting) just starting out and need a business card design with a simple yet slick logo. We provide client focused consultancy support to manage and advise on procurement and acquisition projects for private businesses. Most of our projects are conducted for large well established companies and involve a fair degree of international work, so we would like to reflect that in the design. A large part of the business is also understanding client needs and then connecting them to, or sourcing the right solutions. So we would like to communicate our professionalism, an international focus and our willingness to provide tailored client solutions.

Target Market(s)

Generally we deal with middle to senior executive levels at large companies or with some high wealth private clients/companies. Mostly a conservative group so we want to project a sharp, professional and international image.

Industry/Entity Type

Consulting

Requirements
Must have
• Looking for a simple double sided business card design. Need to have our business name (Valmor Consulting), a person''s name and position title, and our company contact details. Also need a logo that would also convey the international nature of our consultancy.

```html
<!DOCTYPE html>
<html lang="en">
<head>
<meta charset="utf-8">
<title>Valmor Consulting — Business Card</title>
<link rel="stylesheet" href="https://fonts.googleapis.com/css2?family=Arimo:wght@400;700&display=swap">
<style>
  :root {
    --page: #d9d9dc;
    --ink-deep: #00000c;
    --ink-navy: #0a0428;
    --wave-light: rgba(120, 200, 225, 0.55);
    --wave-mid: rgba(30, 140, 185, 0.55);
    --wave-dark: rgba(10, 50, 95, 0.45);
    --frame: #6a7388;
    --text: #ffffff;
    --text-soft: #dfe6ee;
    --mark: #e6e6e6;
    --ghost: #1a1a28;
  }
  * { margin: 0; padding: 0; box-sizing: border-box; }
  html, body { width: 1008px; height: 1200px; overflow: hidden; }
  body {
    background: var(--page);
    font-family: "Arimo", Arial, sans-serif;
    position: relative;
  }
  .card {
    position: absolute;
    left: 72px;
    width: 864px;
    height: 520px;
    overflow: hidden;
    background: linear-gradient(180deg, var(--ink-deep) 0%, #03031a 45%, var(--ink-navy) 100%);
  }
  .card--front { top: 60px; }
  .card--back { top: 620px; }
  .card__art {
    position: absolute;
    inset: 0;
    background: linear-gradient(170deg,
      transparent 0%, transparent 30%,
      var(--wave-light) 45%, var(--wave-mid) 62%,
      var(--wave-dark) 82%, transparent 100%);
  }
  .card__frame {
    position: absolute;
    left: 64px; right: 64px; top: 39px; bottom: 36px;
    border: 2px solid var(--frame);
  }
  .brand {
    position: absolute;
    display: flex;
    flex-direction: column;
    align-items: center;
    color: var(--mark);
    font-weight: 700;
    text-transform: uppercase;
    white-space: nowrap;
  }
  .brand__dot { border-radius: 50%; background: var(--mark); }
  .brand--front { left: 0; right: 0; top: 93px; }
  .brand--front .brand__dot { width: 100px; height: 100px; margin-bottom: 66px; }
  .brand--front .brand__name { font-size: 30px; letter-spacing: 8px; }
  .brand--back { left: 533px; width: 240px; top: 71px; }
  .brand--back .brand__dot { width: 49px; height: 49px; margin-bottom: 26px; }
  .brand--back .brand__name { font-size: 14px; letter-spacing: 3px; }
  .brand--ghost { left: 84px; width: 400px; top: 60px; color: var(--ghost); }
  .brand--ghost .brand__dot { width: 86px; height: 86px; margin-bottom: 64px; background: var(--ghost); }
  .brand--ghost .brand__name { font-size: 22px; letter-spacing: 6px; }
  .contact {
    position: absolute;
    left: 91px;
    top: 276px;
    color: var(--text-soft);
    text-transform: uppercase;
  }
  .contact__headline {
    color: var(--text);
    font-weight: 700;
    font-size: 30px;
    line-height: 33px;
    text-transform: none;
  }
  .contact__line { font-size: 25px; line-height: 30px; letter-spacing: -0.4px; }
  .contact__phone { font-size: 32px; line-height: 34px; letter-spacing: -0.5px; }
</style>
</head>
<body>
  <section class="card card--front">
    <div class="card__art" role="img" aria-label="Flowing blue wave illustration"></div>
    <div class="card__frame"></div>
    <div class="brand brand--front">
      <span class="brand__dot"></span>
      <span class="brand__name">Valmor Consulting</span>
    </div>
  </section>

  <section class="card card--back">
    <div class="card__art" role="img" aria-label="Flowing blue wave illustration"></div>
    <div class="card__frame"></div>
    <div class="brand brand--ghost" aria-hidden="true">
      <span class="brand__dot"></span>
      <span class="brand__name">Valmor Consulting</span>
    </div>
    <div class="brand brand--back">
      <span class="brand__dot"></span>
      <span class="brand__name">Valmor Consulting</span>
    </div>
    <div class="contact">
      <p class="contact__headline">Lorem ipsum dolor sit amet</p>
      <p class="contact__line">Consectetur adipisicing elit</p>
      <p class="contact__line">Sed do eiusmod@mailhaven.com</p>
      <p class="contact__phone">+1234567890</p>
    </div>
  </section>
</body>
</html>
```